Christmas Banner for frontpage of website

New online scarf store just opened needs a Christmas Banner stating Free Delivery (UK only). Also if it could incorporate guaranteed Christmas delivery if ordered before 18th (might be too wordy though?) I would really like it to bring some colour to the page. The page is currently black and white with a pink accent and is very simple which is why I would like something modern and elegant, simple but with some colour. It is a shopify store I understand the banner size should be 950px by 290px the website is www.velmorrow.co.uk

Target Market(s)

Ladies

Industry/Entity Type

Store

Requirements
Should not have
• Not to look tacky.

```html
<!DOCTYPE html>
<html lang="en">
<head>
<meta charset="utf-8">
<title>Velmorrow – Christmas Free Delivery Banner</title>
<link rel="stylesheet" href="https://fonts.googleapis.com/css2?family=Fira+Sans:wght@400;600&family=Fira+Sans+Condensed:wght@700&display=swap">
<style>
  :root {
    --page: #ffffff;
    --frame: #b5b5b5;
    --holly-green: #0b8a45;
    --berry-red: #e8262b;
    --ink: #333333;
  }
  html, body {
    margin: 0;
    padding: 0;
    width: 1200px;
    height: 1001px;
    overflow: hidden;
    background: var(--page);
  }
  .canvas {
    position: relative;
    width: 1200px;
    height: 1001px;
  }
  .banner {
    position: absolute;
    left: 125px;
    top: 355px;
    width: 948px;
    height: 288px;
    border: 1px solid var(--frame);
    background: var(--page);
  }
  .bauble {
    position: absolute;
    left: 153px;
    top: 4px;
    width: 136px;
    height: 262px;
    border-radius: 68px 68px 68px 68px / 120px 120px 68px 68px;
    background: linear-gradient(180deg, rgba(11,138,69,0.55) 0%, rgba(11,138,69,0.35) 42%, var(--berry-red) 48%, #d81f25 100%);
  }
  .stars {
    position: absolute;
    top: 0;
    left: 0;
  }
  .headline {
    position: absolute;
    left: 299px;
    top: 138px;
    margin: 0;
    font-family: "Fira Sans", sans-serif;
    font-weight: 400;
    font-size: 69px;
    line-height: 1;
    letter-spacing: -0.5px;
    color: var(--holly-green);
    white-space: nowrap;
  }
  .headline .region {
    font-family: "Fira Sans Condensed", sans-serif;
    font-weight: 700;
    font-size: 25px;
    letter-spacing: 0;
    margin-left: 3px;
  }
  .cutoff-note {
    position: absolute;
    right: 22px;
    top: 256px;
    margin: 0;
    font-family: "Fira Sans", sans-serif;
    font-size: 18.5px;
    line-height: 1;
    color: var(--ink);
    white-space: nowrap;
  }
</style>
</head>
<body>
<main class="canvas">
  <section class="banner" aria-label="Christmas free delivery banner">
    <div class="bauble" role="img" aria-label="Red swirled Christmas bauble hanging from a dotted green bow"></div>

    <svg class="stars" width="948" height="288" viewBox="0 0 948 288" aria-hidden="true">
      <g fill="var(--berry-red)">
        <polygon points="121,102 125,112 135,113 127,119 130,130 121,124 112,130 115,119 107,113 117,112"/>
        <polygon points="868,108 872,118 883,119 875,126 878,137 868,131 858,137 861,126 853,119 864,118"/>
        <polygon points="856,134 858,139 863,139 859,142 861,147 856,144 851,147 853,142 849,139 854,139"/>
        <polygon points="845,123 846,126 849,126 847,128 848,131 845,129 842,131 843,128 841,126 844,126"/>
        <polygon points="324,107 325,110 328,110 326,112 327,115 324,113 321,115 322,112 320,110 323,110"/>
      </g>
      <g fill="var(--holly-green)">
        <polygon points="107,128 109,133 114,133 110,136 112,141 107,138 102,141 104,136 100,133 105,133"/>
        <polygon points="96,117 97,120 100,120 98,122 99,125 96,123 93,125 94,122 92,120 95,120"/>
        <polygon points="332,93 334,98 339,98 335,101 337,106 332,103 327,106 329,101 325,98 330,98"/>
      </g>
    </svg>

    <h1 class="headline">FREE DELIVERY<span class="region">(UK only).</span></h1>
    <p class="cutoff-note">Guaranteed Christmas delivery if ordered before 18th.</p>
  </section>
</main>
</body>
</html>
```